Website Landing Page for Medical Recruitment

Looking for a landing page to add to our existing website. The objective of the page is to recruit new clinical staff for various departments within PineHollow Medical Center (non-profit hospital in the Richmond, TX area).

We would like the page to be modern, professional, and non-cluttered. Please include call-to-actions and include a button that will navigate to the page where candidates can submit their applications (this page already exists).

Target Market(s)

25-35-year-olds who live in the Houston and Richmond area with medical experience.

Industry/Entity Type

Medical/Health

Font styles to use
Sans Serif

Colors
0054AA
0677BA
7BADD7
CADEEF
E8F1F8

Requirements
Must have
• A "call to action"; a button that navigates to pinehollowmedcenter.example/careers

```html
<!DOCTYPE html>
<html lang="en">
<head>
<meta charset="utf-8">
<title>PineHollow Medical Center – Careers</title>
<link rel="stylesheet" href="https://fonts.googleapis.com/css2?family=Poppins:wght@400;500;600;700&family=Bebas+Neue&display=swap">
<style>
:root{
  --brand:#2b64a8;
  --brand-dark:#0054aa;
  --brand-mid:#0677ba;
  --sky:#7badd7;
  --mist:#cadeef;
  --ice:#e8f1f8;
  --ink:#1d1d1d;
  --muted:#6b6b6b;
  --white:#ffffff;
}
*{box-sizing:border-box;margin:0;padding:0}
html,body{width:1200px;height:3960px;overflow:hidden}
body{font-family:"Poppins",sans-serif;color:var(--ink);background:var(--white);position:relative}
a{text-decoration:none;color:inherit}
.abs{position:absolute}
.btn{position:absolute;display:flex;align-items:center;justify-content:center;border-radius:30px;font-weight:600;font-size:14px;letter-spacing:.3px}
.btn--solid{background:var(--brand);color:var(--white)}
.btn--light{background:var(--white);color:var(--brand)}
.photo{position:absolute}

/* header */
.site-header{position:absolute;left:0;top:0;width:1200px;height:89px;background:var(--white)}
.brand{position:absolute;left:58px;top:20px;display:flex;align-items:center;gap:10px;color:var(--brand);font-weight:600;font-size:24px}
.brand__dot{width:40px;height:40px;border-radius:50%;background:var(--brand)}
.nav a{position:absolute;top:36px;font-size:13px;font-weight:500;color:#555}
.nav a.is-active{color:var(--brand)}

/* hero */
.hero{position:absolute;left:0;top:89px;width:1200px;height:638px;background:linear-gradient(100deg,#3f6fab 0%,#5b87bf 45%,#6d94c6 100%)}
.hero__title{position:absolute;left:61px;top:128px;font-family:"Bebas Neue",sans-serif;font-size:94px;line-height:90px;color:var(--white);letter-spacing:-1px}
.hero__text{position:absolute;left:61px;top:329px;width:420px;font-size:12px;line-height:22px;color:var(--white)}
.hero__ring{position:absolute;left:722px;top:190px;width:330px;height:330px;border-radius:50%;border:2px solid rgba(255,255,255,.25);background:rgba(255,255,255,.08)}

/* job offers */
.section-title{position:absolute;font-weight:600;font-size:36px;color:var(--ink)}
.job-card{position:absolute;top:900px;width:247px;height:225px;border:1px solid #e2e2e2;border-radius:4px;box-shadow:0 1px 4px rgba(0,0,0,.06);padding:24px 22px}
.job-card h3{font-size:15px;font-weight:600;margin-bottom:4px}
.job-card .sub{font-size:13px;color:var(--brand);margin-bottom:18px}
.job-card p{font-size:11.5px;line-height:22px;color:var(--muted)}
.job-card .more{position:absolute;left:26px;bottom:40px;font-size:11px;font-weight:700;color:var(--brand)}

/* promo band */
.band{position:absolute;left:0;width:1200px;background:var(--brand);color:var(--white)}
.band__mark{position:absolute;left:104px;top:26px;width:170px;height:170px;border-radius:50%;background:var(--white)}
.band__rule{position:absolute;left:326px;top:24px;width:1px;height:176px;background:rgba(255,255,255,.25)}
.band h2{position:absolute;font-weight:500;font-size:38px;letter-spacing:.5px}
.band p{position:absolute;font-size:12px;line-height:22px}

/* about */
.about p{position:absolute;left:61px;width:510px;font-size:12px;line-height:22.5px;color:var(--muted)}
.play{position:absolute;left:678px;top:1750px;width:58px;height:58px;border-radius:50%;background:var(--brand);display:flex;align-items:center;justify-content:center}

/* testimonials */
.quote-text{position:absolute;left:647px;top:2122px;width:460px;font-size:12px;line-height:22.5px;color:var(--muted)}
.arrow{position:absolute;top:2266px;width:38px;height:38px;border-radius:50%;display:flex;align-items:center;justify-content:center}

/* reach */
.reach{position:absolute;left:0;top:2391px;width:1200px;height:525px;background:linear-gradient(100deg,#3a6aa8 0%,#4f7db8 55%,#6a91c2 100%)}
.reach__portrait{position:absolute;left:730px;top:26px;width:374px;height:374px;border-radius:50%;background:radial-gradient(circle at 55% 40%,#f1f3f5 0%,#d9dde3 50%,#b4bcc7 100%)}
.reach h2{position:absolute;left:61px;top:68px;font-size:38px;font-weight:600;color:var(--white)}
.reach p{position:absolute;left:61px;width:560px;font-size:12px;line-height:22.5px;color:var(--white)}
.reach .lead{font-size:15px;font-weight:600}
.feature{position:absolute;top:2692px;width:170px;text-align:center;color:var(--white);font-size:14px;font-weight:600}
.feature svg{display:block;margin:0 auto 8px}

/* news */
.news{position:absolute;top:3257px;width:337px}
.news__img{position:relative;width:337px;height:225px}
.news__date{position:absolute;left:0;top:0;width:50px;height:61px;background:var(--brand);color:var(--white);text-align:center;font-size:16px;font-weight:600;padding-top:6px;line-height:18px}
.news__date small{display:block;font-size:11px;font-weight:400}
.news h3{font-size:15px;font-weight:600;line-height:26px;margin-top:16px}
.news p{font-size:11.5px;line-height:22.5px;color:var(--muted);margin-top:16px}
.news .more{display:block;font-size:11px;font-weight:700;color:var(--brand);margin-top:16px}

/* footer */
.site-footer{position:absolute;left:0;top:3748px;width:1200px;height:212px;background:var(--brand);color:var(--white)}
.contact-line{position:absolute;left:61px;display:flex;align-items:center;gap:10px;font-size:12px}
.social{position:absolute;top:126px;width:30px;height:30px;border-radius:50%;background:var(--white)}
.footer-brand{position:absolute;left:473px;top:52px;display:flex;align-items:center;gap:10px;font-size:24px;font-weight:600}
.footer-brand span.dot{width:40px;height:40px;border-radius:50%;background:var(--white)}
.copyright{position:absolute;left:0;width:1200px;top:138px;text-align:center;font-size:11px}
.subscribe{position:absolute;left:828px;top:82px;width:312px;height:46px;border:1px solid var(--white);border-radius:30px;display:flex;overflow:hidden}
.subscribe span{flex:1;font-size:12px;padding:14px 18px;color:rgba(255,255,255,.9)}
.subscribe b{width:126px;background:var(--white);color:var(--brand);display:flex;align-items:center;justify-content:center;font-size:14px;border-radius:0 30px 30px 0}
</style>
</head>
<body>

<header class="site-header">
  <a class="brand" href="#"><span class="brand__dot"></span>PineHollow Medical Center</a>
  <nav class="nav">
    <a class="is-active" style="left:611px" href="#">Home</a>
    <a style="left:684px" href="#">About Us</a>
    <a style="left:776px" href="#">Vacancies</a>
    <a style="left:877px" href="#">Contact Us</a>
  </nav>
  <a class="btn btn--solid" style="left:990px;top:23px;width:150px;height:45px" href="https://pinehollowmedcenter.example/careers">APPLY NOW</a>
</header>

<section class="hero" role="img" aria-label="Smiling nurse in scrubs with a team of clinicians behind her, tinted blue">
  <div class="hero__ring"></div>
  <h1 class="hero__title">NEW OFFERS ARE<br>WAITING FOR YOU</h1>
  <p class="hero__text">Lorem Ipsum is simply dummy text of the printing and typesetting industry. Lorem Ipsum has been the industry's standard dummy text ever since the 1500s.</p>
  <a class="btn btn--light" style="left:61px;top:424px;width:149px;height:43px" href="https://pinehollowmedcenter.example/careers">APPLY NOW</a>
</section>

<h2 class="section-title" style="left:0;width:1107px;text-align:center;top:814px">JOB OFFERS</h2>
<article class="job-card" style="left:60px"><h3>Job Position</h3><div class="sub">Lorem ipsum</div><p>Lorem ipsum is simply dummy text and printing typesetting.</p><a class="more" href="#">READ MORE</a></article>
<article class="job-card" style="left:338px"><h3>Job Position</h3><div class="sub">Lorem ipsum</div><p>Lorem ipsum is simply dummy text and printing typesetting.</p><a class="more" href="#">READ MORE</a></article>
<article class="job-card" style="left:615px"><h3>Job Position</h3><div class="sub">Lorem ipsum</div><p>Lorem ipsum is simply dummy text and printing typesetting.</p><a class="more" href="#">READ MORE</a></article>
<article class="job-card" style="left:893px"><h3>Job Position</h3><div class="sub">Lorem ipsum</div><p>Lorem ipsum is simply dummy text and printing typesetting.</p><a class="more" href="#">READ MORE</a></article>
<a class="btn btn--solid" style="left:525px;top:1162px;width:150px;height:44px" href="#">VIEW MORE</a>

<section class="band" style="top:1297px;height:224px">
  <div class="band__mark"></div>
  <div class="band__rule"></div>
  <h2 style="left:364px;top:38px">LOREM IPSUM IS SIMPLY DUMMY TEXT</h2>
  <p style="left:364px;top:89px;width:760px">Lorem ipsum is simply dummy text of the printing and typesetting industry. Lorem Ipsum has been the industry's standard dummy text ever since the 1500s.</p>
  <a class="btn btn--light" style="left:364px;top:144px;width:149px;height:43px" href="https://pinehollowmedcenter.example/careers">APPLY NOW</a>
</section>

<section class="about">
  <h2 class="section-title" style="left:61px;top:1616px">ABOUT US</h2>
  <p style="top:1685px">Lorem ipsum is simply dummy text of the printing and typesetting industry. Lorem Ipsum has been the industry's standard dummy text ever since the 1500s, when an unknown printer took a galley of type and scrambled it to make a type specimen book. It has survived not only five centuries, but also the leap into electronic typesetting, remaining essentially unchanged.</p>
  <p style="top:1820px">It was popularised in the 1960s with the release of printed sheets containing Lorem Ipsum passages, and more recently with desktop publishing software that includes many versions of Lorem Ipsum.</p>
  <a class="btn btn--solid" style="left:60px;top:1919px;width:149px;height:43px" href="#">READ MORE</a>
  <div class="photo" role="img" aria-label="Three clinicians reviewing notes together in a hospital" style="left:707px;top:1646px;width:435px;height:299px;background:linear-gradient(110deg,#7e93a8 0%,#c9cdd2 45%,#e6e2dc 70%,#b79479 100%)"></div>
  <div class="play"><svg width="18" height="18" viewBox="0 0 18 18"><path d="M6 4l7 5-7 5z" fill="#fff"/></svg></div>
</section>

<section class="clients">
  <div class="abs" style="left:0;top:2068px;width:599px;height:149px;background:var(--brand)"></div>
  <div class="photo" role="img" aria-label="Client portrait" style="left:0;top:2136px;width:92px;height:164px;background:linear-gradient(160deg,#d8c8b8,#a88f7a)"></div>
  <div class="photo" role="img" aria-label="Client portrait, woman with glasses" style="left:124px;top:2136px;width:196px;height:164px;background:linear-gradient(160deg,#e9e7e4,#c9b9a4)"></div>
  <div class="photo" role="img" aria-label="Client portrait, man in denim shirt" style="left:352px;top:2136px;width:195px;height:164px;background:linear-gradient(160deg,#f0efee,#6f8db0)"></div>
  <h2 class="section-title" style="left:647px;top:2066px">WHAT OUR CLIENTS SAY</h2>
  <p class="quote-text">Lorem Ipsum is simply dummy text of the printing and typesetting industry. Lorem Ipsum has been the industry's standard dummy text ever since the 1500s, when an unknown printer took a galley of type and scrambled it to make a type specimen book.</p>
  <div class="abs" style="left:647px;top:2234px;font-size:11px;font-weight:700;color:var(--brand)">– CLIENT NAME</div>
  <div class="arrow" style="left:654px;background:var(--brand)"><svg width="12" height="12" viewBox="0 0 12 12"><path d="M8 1L3 6l5 5" stroke="#fff" stroke-width="1.6" fill="none"/></svg></div>
  <div class="arrow" style="left:708px;background:#c9c9c9"><svg width="12" height="12" viewBox="0 0 12 12"><path d="M4 1l5 5-5 5" stroke="#fff" stroke-width="1.6" fill="none"/></svg></div>
</section>

<section class="reach" role="img" aria-label="Blue-tinted hospital corridor backdrop">
  <div class="reach__portrait" role="img" aria-label="Portrait of a smiling doctor in a white coat"></div>
  <h2>REACH YOUR DREAM</h2>
  <p style="top:127px">Lorem Ipsum is simply dummy text of the printing and typesetting industry. Lorem Ipsum has been the industry's standard dummy text ever since the 1500s.</p>
  <p class="lead" style="top:182px">Lorem Ipsum – is simply – dummy text.</p>
  <p style="top:210px">Lorem Ipsum is simply dummy text of the printing and typesetting industry. Lorem Ipsum has been the industry's standard dummy text ever since the 1500s, when an unknown printer took a galley of type and scrambled it to make a type specimen book. <u style="font-weight:600">READ MORE</u></p>
</section>
<div class="feature" style="left:49px"><svg width="44" height="44" viewBox="0 0 44 44" fill="none" stroke="#fff" stroke-width="2"><circle cx="22" cy="12" r="8"/><path d="M22 12V7M22 12l4 3"/><circle cx="22" cy="26" r="4"/><path d="M14 38c0-5 4-8 8-8s8 3 8 8z"/><path d="M4 38h36"/></svg>Daily supply work</div>
<div class="feature" style="left:230px"><svg width="44" height="44" viewBox="0 0 44 44" fill="none" stroke="#fff" stroke-width="2"><rect x="4" y="7" width="36" height="33" rx="3"/><path d="M4 15h36M13 3v8M31 3v8"/><path d="M12 22h4M20 22h4M28 22h4M12 29h4M20 29h4M28 29h4" stroke-width="3"/></svg>Long-term roles</div>
<div class="feature" style="left:419px"><svg width="44" height="44" viewBox="0 0 44 44" fill="none" stroke="#fff" stroke-width="2"><rect x="3" y="10" width="32" height="24" rx="3"/><path d="M13 10V5h12v5M3 20h32"/><circle cx="34" cy="33" r="8" fill="#fff"/><path d="M30 33l3 3 5-6" stroke="#2b64a8"/></svg>A permanent job</div>
<a class="btn btn--light" style="left:60px;top:2796px;width:180px;height:44px" href="#">DISCOVER MORE</a>

<section class="band" style="top:2916px;height:165px">
  <h2 style="left:61px;top:32px;font-weight:600">OUR VACANCIES</h2>
  <p style="left:61px;top:88px;width:790px;font-size:11px;line-height:20px">Lorem Ipsum is simply dummy text of the printing and typesetting industry. Lorem Ipsum has been the industry's standard dummy text ever since the 1500s, when an unknown printer took a galley of type and scrambled it to make a type specimen book.</p>
  <a class="btn btn--light" style="left:990px;top:62px;width:150px;height:44px" href="https://pinehollowmedcenter.example/careers">APPLY NOW</a>
</section>

<h2 class="section-title" style="left:0;width:1200px;text-align:center;top:3170px">LATEST NEWS</h2>
<article class="news" style="left:60px">
  <div class="news__img" role="img" aria-label="Hospital reception with patients waiting" style="background:linear-gradient(120deg,#c6ccd2,#8e9aa6 60%,#5d6f82)"><div class="news__date">06<small>Aug</small></div></div>
  <h3>Lorem ipsum is simply dummt text and printing typesetting.</h3>
  <p>Lorem Ipsum is simply dummy text of the printing and typesetting industry. Lorem Ipsum has been the industry's standard dummy text ever...</p>
  <a class="more" href="#">READ MORE</a>
</article>
<article class="news" style="left:432px">
  <div class="news__img" role="img" aria-label="Lab technician working at a computer" style="background:linear-gradient(120deg,#d5d8dc,#9aa4ae 55%,#4c5d70)"><div class="news__date">05<small>Aug</small></div></div>
  <h3>Lorem ipsum is simply dummt text and printing typesetting.</h3>
  <p>Lorem Ipsum is simply dummy text of the printing and typesetting industry. Lorem Ipsum has been the industry's standard dummy text ever...</p>
  <a class="more" href="#">READ MORE</a>
</article>
<article class="news" style="left:804px">
  <div class="news__img" role="img" aria-label="Pharmacist standing between medicine shelves" style="background:linear-gradient(120deg,#eef0f2,#cfd5db 55%,#8f9aa6)"><div class="news__date">04<small>Aug</small></div></div>
  <h3>Lorem ipsum is simply dummt text and printing typesetting.</h3>
  <p>Lorem Ipsum is simply dummy text of the printing and typesetting industry. Lorem Ipsum has been the industry's standard dummy text ever...</p>
  <a class="more" href="#">READ MORE</a>
</article>

<footer class="site-footer">
  <div class="contact-line" style="top:42px"><svg width="14" height="14" viewBox="0 0 14 14"><path d="M7 1a4 4 0 0 0-4 4c0 3 4 8 4 8s4-5 4-8a4 4 0 0 0-4-4z" fill="#fff"/><circle cx="7" cy="5" r="1.5" fill="#2b64a8"/></svg>Lorem Ipsum is simply dummy text of the.</div>
  <div class="contact-line" style="top:68px"><svg width="14" height="14" viewBox="0 0 14 14"><path d="M3 1l2 3-1 2c1 2 2 3 4 4l2-1 3 2-1 2C6 13 1 8 1 2z" fill="#fff"/></svg>555 014 2290</div>
  <div class="contact-line" style="top:93px"><svg width="14" height="14" viewBox="0 0 14 14" fill="none" stroke="#fff" stroke-width="1.3"><rect x="1" y="3" width="12" height="9"/><path d="M1 3l6 5 6-5"/></svg>info@pinehollowmedcenter.example</div>
  <div class="social" style="left:61px"></div>
  <div class="social" style="left:98px"></div>
  <div class="social" style="left:135px"></div>
  <div class="footer-brand"><span class="dot"></span>PineHollow Medical Center</div>
  <div class="copyright">© PINEHOLLOW MEDICAL CENTER – 2022. All Rights Reserved.</div>
  <div class="subscribe"><span>Enter email here...</span><b>SUBSCRIBE</b></div>
</footer>

</body>
</html>
```